Design some Business Cards

I need a business card designed, in English on one side, and in Russian on the other side, which will incorporate my client’s logo (logo in different formats is in zip folder attached). The name, details/info required on the business card are in the document in the zip folder.

Please let me know if you have any questions. I will provide feedback on the entries as quickly as I can.

Regards.

```html
<!DOCTYPE html>
<html lang="en">
<head>
<meta charset="utf-8">
<title>Torvanel Invest — Business Cards</title>
<link rel="stylesheet" href="https://fonts.googleapis.com/css2?family=Montserrat:wght@400;500;600&display=swap">
<style>
  :root {
    --page-bg: #2b2b2b;
    --card-black: #050505;
    --strip-white: #ffffff;
    --accent-orange: #f0922b;
    --accent-blue: #2f7fc8;
    --brand-ink: #2a5f99;
    --text-light: #f2f2f2;
    --text-muted: #c9c9c9;
    --divider: #8a8a8a;
  }
  * { box-sizing: border-box; margin: 0; padding: 0; }
  html, body { width: 1200px; height: 900px; overflow: hidden; }
  body {
    background: var(--page-bg);
    font-family: "Montserrat", sans-serif;
    position: relative;
  }
  .business-card {
    position: absolute;
    left: 267px;
    width: 666px;
    height: 380px;
    background: var(--card-black);
    display: flex;
    box-shadow: 0 12px 30px rgba(0,0,0,0.45);
  }
  .card-english { top: 50px; }
  .card-russian { top: 470px; }
  .brand-strip {
    width: 118px;
    height: 100%;
    background: var(--strip-white);
    display: flex;
    align-items: center;
    justify-content: center;
  }
  .brand-name {
    transform: rotate(-90deg);
    white-space: nowrap;
    font-size: 28px;
    font-weight: 500;
    letter-spacing: 3px;
    color: var(--brand-ink);
  }
  .card-body {
    flex: 1;
    position: relative;
  }
  .contact-block {
    position: absolute;
    left: 220px;
    top: 112px;
    padding-left: 26px;
    border-left: 2px solid var(--divider);
  }
  .card-russian .contact-block { top: 100px; }
  .person-name {
    color: var(--accent-orange);
    font-weight: 600;
    font-size: 22px;
    line-height: 1.1;
  }
  .person-role {
    color: var(--text-muted);
    font-size: 14px;
    margin-top: 4px;
    margin-bottom: 12px;
  }
  .contact-list { list-style: none; }
  .contact-item {
    display: flex;
    align-items: center;
    height: 26px;
    color: var(--text-light);
    font-size: 15px;
    white-space: nowrap;
  }
  .contact-icon {
    width: 16px;
    height: 16px;
    margin-right: 14px;
    margin-left: -4px;
    flex-shrink: 0;
  }
</style>
</head>
<body>
  <article class="business-card card-english" lang="en">
    <div class="brand-strip"><span class="brand-name">TORVANEL INVEST</span></div>
    <div class="card-body">
      <div class="contact-block">
        <h1 class="person-name">Marta Kovalenko</h1>
        <p class="person-role">Director</p>
        <ul class="contact-list">
          <li class="contact-item">
            <svg class="contact-icon" viewBox="0 0 24 24" aria-hidden="true"><path fill="var(--accent-blue)" d="M6.6 10.8a15.1 15.1 0 0 0 6.6 6.6l2.2-2.2a1 1 0 0 1 1-.25 11.4 11.4 0 0 0 3.6.57 1 1 0 0 1 1 1V20a1 1 0 0 1-1 1A17 17 0 0 1 3 4a1 1 0 0 1 1-1h3.5a1 1 0 0 1 1 1c0 1.25.2 2.45.57 3.57a1 1 0 0 1-.25 1z"/></svg>
            +34 600 412 385</li>
          <li class="contact-item">
            <svg class="contact-icon" viewBox="0 0 24 24" aria-hidden="true"><rect x="3" y="6" width="18" height="12" fill="none" stroke="var(--accent-blue)" stroke-width="2"/><path d="M3 6l9 7 9-7" fill="none" stroke="var(--accent-blue)" stroke-width="2"/></svg>
            marta@torvanelinvest.com.ua</li>
          <li class="contact-item">
            <svg class="contact-icon" viewBox="0 0 24 24" aria-hidden="true"><g fill="none" stroke="var(--accent-blue)" stroke-width="2"><circle cx="12" cy="12" r="9"/><ellipse cx="12" cy="12" rx="4" ry="9"/><path d="M3 12h18"/></g></svg>
            www.torvanelinvest.com.ua</li>
        </ul>
      </div>
    </div>
  </article>

  <article class="business-card card-russian" lang="ru">
    <div class="brand-strip"><span class="brand-name">TORVANEL INVEST</span></div>
    <div class="card-body">
      <div class="contact-block">
        <h2 class="person-name">Марта Коваленко</h2>
        <p class="person-role">Директор</p>
        <ul class="contact-list">
          <li class="contact-item">
            <svg class="contact-icon" viewBox="0 0 24 24" aria-hidden="true"><path fill="var(--accent-blue)" d="M6.6 10.8a15.1 15.1 0 0 0 6.6 6.6l2.2-2.2a1 1 0 0 1 1-.25 11.4 11.4 0 0 0 3.6.57 1 1 0 0 1 1 1V20a1 1 0 0 1-1 1A17 17 0 0 1 3 4a1 1 0 0 1 1-1h3.5a1 1 0 0 1 1 1c0 1.25.2 2.45.57 3.57a1 1 0 0 1-.25 1z"/></svg>
            +38 050 730 44 18</li>
          <li class="contact-item">
            <svg class="contact-icon" viewBox="0 0 24 24" aria-hidden="true"><path fill="var(--accent-blue)" d="M6.6 10.8a15.1 15.1 0 0 0 6.6 6.6l2.2-2.2a1 1 0 0 1 1-.25 11.4 11.4 0 0 0 3.6.57 1 1 0 0 1 1 1V20a1 1 0 0 1-1 1A17 17 0 0 1 3 4a1 1 0 0 1 1-1h3.5a1 1 0 0 1 1 1c0 1.25.2 2.45.57 3.57a1 1 0 0 1-.25 1z"/></svg>
            +34 600 412 385</li>
          <li class="contact-item">
            <svg class="contact-icon" viewBox="0 0 24 24" aria-hidden="true"><rect x="3" y="6" width="18" height="12" fill="none" stroke="var(--accent-blue)" stroke-width="2"/><path d="M3 6l9 7 9-7" fill="none" stroke="var(--accent-blue)" stroke-width="2"/></svg>
            marta@torvanelinvest.com.ua</li>
          <li class="contact-item">
            <svg class="contact-icon" viewBox="0 0 24 24" aria-hidden="true"><g fill="none" stroke="var(--accent-blue)" stroke-width="2"><circle cx="12" cy="12" r="9"/><ellipse cx="12" cy="12" rx="4" ry="9"/><path d="M3 12h18"/></g></svg>
            www.torvanelinvest.com.ua</li>
        </ul>
      </div>
    </div>
  </article>
</body>
</html>
```